Book cover for publishing doctoral research about various national styles of piano playing.

I need a book cover for a publication of a doctoral research with regard to styles of piano performance characteristic to various nations.

Any images or graphics are optional, typography seems most important, but please feel free to be creative.

I attach the barcode, qsr and publisher's logo in the next few days. (Logo is still being designed).

For various reasons the size of the book is not completely decided yet. Please create your design in 7" x 10", but if at all possible, I would like to ask for files of two sizes, also including 8.5" x 11" in the final submission.

I am looking for a design that looks professional, probably simple, but I am open to any suggestions.

Dear Designers,I would like to thank you all for participation and submitting so many high-quality designs.My final decision was based on the feedback I received from my professional colleagues and potential readers.I would like to wish you all the best for the future.Best wishes,Tadeusz Added Monday, December 21, 2015

Pianists, students, music professionals

Publishing

• Title: Unfolding Seven Harbour Lullabies
• Subtitle: Memories and departures
• Author: Tadeusz Jarocki
• Space for my logo on the front page and the spine.
• On the back page, please include some space for a short biography, 'barcode' and 'qsr' code.
• Please include whatever else you consider necessary.
• Would it be possible to use the same cover to a e-book edition?

```html
<!DOCTYPE html>
<html lang="en">
<head>
<meta charset="utf-8">
<title>Unfolding Seven Harbour Lullabies – Cover</title>
<link href="https://fonts.googleapis.com/css2?family=Didact+Gothic&family=Oswald:wght@400&family=Pinyon+Script&family=PT+Sans:wght@700&display=swap" rel="stylesheet">
<style>
  :root {
    --backdrop: #e9e6e1;
    --paper: #ffffff;
    --title-gold: #c9c01c;
    --kicker-grey: #8a8a8a;
    --maroon: #8b5552;
    --ink-white: #ffffff;
    --photo-dark: #1f3a3f;
    --photo-teal: #3f6a6c;
    --photo-cream: #e8dcb8;
    --photo-warm: #b7786a;
    --logo-fill: rgba(240, 232, 210, 0.75);
    --logo-ink: #9c958a;
  }
  * { margin: 0; padding: 0; box-sizing: border-box; }
  html, body {
    width: 1200px; height: 1200px; overflow: hidden;
    background: var(--backdrop);
  }
  .cover {
    position: absolute; left: 250px; top: 100px;
    width: 700px; height: 1000px;
    background: var(--paper);
    box-shadow: 0 8px 30px rgba(0,0,0,0.18);
    overflow: hidden;
  }
  .title-block {
    position: absolute; left: 0; top: 0; width: 100%; height: 180px;
    background: var(--paper);
    padding: 42px 44px 0 44px;
  }
  .title-kicker {
    font-family: "Didact Gothic", sans-serif;
    font-size: 30px; letter-spacing: 0.42em;
    color: var(--kicker-grey);
    white-space: nowrap;
  }
  .title-main {
    font-family: "Oswald", sans-serif;
    font-weight: 400;
    font-size: 76px; line-height: 1;
    color: var(--title-gold);
    letter-spacing: 0.01em;
    margin-top: 6px;
    white-space: nowrap;
  }
  .title-rule {
    position: absolute; left: 0; top: 180px; width: 100%; height: 4px;
    background: var(--maroon);
  }
  .cover-photo {
    position: absolute; left: 0; top: 184px; width: 100%; height: 746px;
    background:
      radial-gradient(ellipse 45% 30% at 88% 20%, rgba(183,120,106,0.75), transparent 70%),
      radial-gradient(ellipse 60% 35% at 55% 80%, var(--photo-cream), transparent 70%),
      linear-gradient(155deg, var(--photo-dark) 0%, var(--photo-teal) 40%, #8a8e7c 62%, var(--photo-cream) 85%);
  }
  .subtitle {
    position: absolute; left: 0; top: 206px; width: 100%;
    text-align: center;
    font-family: "Pinyon Script", cursive;
    font-size: 46px; color: var(--ink-white);
  }
  .logo-slot {
    position: absolute; left: 40px; top: 856px;
    width: 120px; height: 56px;
    background: var(--logo-fill);
    display: flex; align-items: center; justify-content: center;
    font-family: "Didact Gothic", sans-serif;
    font-size: 34px; color: var(--logo-ink);
  }
  .author-band {
    position: absolute; left: 0; top: 930px; width: 100%; height: 70px;
    background: var(--maroon);
    display: flex; align-items: center; justify-content: flex-end;
    padding-right: 36px;
  }
  .author-name {
    font-family: "PT Sans", sans-serif;
    font-weight: 700; font-size: 26px;
    color: var(--ink-white);
  }
</style>
</head>
<body>
  <main class="cover">
    <header class="title-block">
      <div class="title-kicker">Unfolding Seven</div>
      <h1 class="title-main">HARBOUR LULLABIES</h1>
    </header>
    <div class="title-rule"></div>
    <div class="cover-photo" role="img" aria-label="Close-up photograph of piano keys in soft teal and cream light"></div>
    <p class="subtitle">Memories and departures</p>
    <div class="logo-slot">logo</div>
    <footer class="author-band">
      <span class="author-name">Tadeusz Jarocki</span>
    </footer>
  </main>
</body>
</html>
```